Brenwo Tiling Solutions Needs A Web Design

We have been a sole trader but now started a new company. We need a web page designed around our new company. We are wall and floor tilers with over 20 years experience.
A Gold Coast family owned business, with over 20 years of experience, Dalton Krusey is proud to be a trusted name for all aspects of Wall and Floor Tiling Services servicing the Gold Coast to Brisbane, Tweed Heads to Mt Tamborine.

With an eye for detail we strive for perfection with the resources to work closely with designers, architects, contractors, and home owners, delivering the best possible service in wall and floor tiling.

We will be more than glad to provide our expertise and can consult or advice you to help you make the decisions that are right for you.

Renovations should always be seen as an investment not an expense. With an ultimate goal of utmost satisfaction, our trained and qualified tradesmen will provide you exceptional services. We are well equipped with latest tools and techniques to ensure that everything is done correctly with attention paid to the smallest details.
Updates

Hello I may not have been very clear. My husband Dalton Krusey is a tiler and we used just a basic PDF flyer "Company profile" when sending our quotations. He now has decided to use a company name and so I would like a web design page for this company "Brenwo Tiling Solutions Pty Ltd" I would like to use the information as stated (in the company profile PDF) BUT under the name Brenwo - I will look into a more detailed look into the description of the job and repost the details - unfortunately I will not be able to do sometime in the next 2 days. I will then repost. My apologies for this Thank You Mae-Lin Krusey

Target Market(s)

Our clients we are aiming at are Builders domestic(homes) and commercial (shops, duplexs & 3 storey units, resort pools) plus home owners looking to renovate existing tiled areas or lay new tiles to new homes. Internal pool and pool surround

Number of Pages Required

3 page

Font styles to use
Serif

Colors
9bcb3b
ec1f27
fbed22

Requirements
Must have
• We like fluro green and black colours. and use the name Dalton Krusey (the owner) as he does the tiling labour and is the one with the expertise.
• The final design should communicate professional workmanship. quality and expertise in ALL aspects of tiling,We have pride in our workmanship and do not cut corners so that the job is done right the first time to the correct standards. Our good name is our reputation.
• I have attached a logo which we would like in fluro green and black. The person in the logo has a hammer - we want to get rid of the hammer as that is for carpentry and we are floor tilers. If another tool ie mallet can be replaced. Can you do that?
Nice to have
• Photos - highlights stand out - nice borders. classic design.

```html
<!DOCTYPE html>
<html lang="en">
<head>
<meta charset="utf-8">
<title>Brenwo Tiling Solutions Pty Ltd – Wall and Floor Tiling Specialist</title>
<link href="https://fonts.googleapis.com/css2?family=Roboto:wght@300;400;500;700;900&display=swap" rel="stylesheet">
<style>
:root{
  --green:#8cc63f;
  --green-dark:#6fa52a;
  --red:#e8262b;
  --yellow:#fbed22;
  --ink:#222;
  --text:#555;
  --grey-bg:#f1f1f1;
  --white:#fff;
}
*{box-sizing:border-box;margin:0;padding:0}
html,body{width:1200px;height:2312px;overflow:hidden}
body{font-family:'Roboto',Arial,sans-serif;color:var(--text);background:var(--white);position:relative}
.container{position:absolute;left:64px;width:1072px}

/* header */
.site-header{position:absolute;top:0;left:0;width:1200px;height:84px;background:linear-gradient(90deg,var(--yellow) 0%,#d8e84a 18%,#fff 42%,#fff 100%)}
.brand{position:absolute;left:64px;top:14px;display:flex;align-items:center;gap:14px}
.brand-mark{width:44px;height:44px;background:var(--ink);border-radius:50%}
.brand-name{font-weight:700;font-size:20px;color:var(--ink);letter-spacing:.5px;line-height:1.1}
.brand-tag{font-size:12px;color:var(--red);font-weight:500;letter-spacing:1px;margin-top:4px}
.call{position:absolute;right:64px;top:26px;display:flex;align-items:center;gap:10px;color:var(--red);font-weight:700;font-size:17px}

/* nav */
.main-nav{top:84px;height:28px;background:var(--green);display:flex}
.main-nav a{display:block;height:28px;line-height:28px;padding:0 26px;color:#fff;font-size:12px;font-weight:700;text-decoration:none;letter-spacing:.5px}
.main-nav a.active{background:var(--red)}

/* hero */
.hero{top:112px;height:460px;background:linear-gradient(160deg,#3f4a3c 0%,#7b8b76 35%,#c9d3cf 60%,#5f6e5c 100%)}
.hero-copy{position:absolute;left:0;right:0;top:270px;text-align:center;color:#fff}
.hero-copy h1{font-size:44px;font-weight:700;letter-spacing:1px;text-shadow:0 2px 6px rgba(0,0,0,.5)}
.hero-copy p{font-size:22px;margin-top:14px;text-shadow:0 2px 6px rgba(0,0,0,.5)}
.hero-dots{position:absolute;top:400px;left:0;right:0;display:flex;justify-content:center;gap:10px}
.hero-dots span{width:11px;height:11px;border-radius:50%;background:rgba(255,255,255,.6)}
.hero-dots span.on{background:#fff}
.hero-arrow{position:absolute;top:210px;width:34px;height:50px;background:rgba(0,0,0,.35)}

/* welcome */
.welcome{top:612px;height:260px}
.welcome-text{position:absolute;left:0;width:660px}
.welcome h2{font-size:22px;font-weight:700;color:var(--ink);padding-bottom:12px;border-bottom:1px solid #ddd}
.welcome p{font-size:13px;line-height:1.6;margin-top:14px}
.btn{display:inline-block;background:var(--green);color:#fff;font-size:12px;font-weight:700;padding:10px 20px;letter-spacing:.5px}
.welcome .btn{position:absolute;top:210px;left:0}
.reviews{position:absolute;left:720px;top:14px;width:352px;height:232px;background:var(--green);padding:18px 22px;color:#fff}
.reviews h3{font-size:22px;font-weight:700;color:var(--ink)}
.reviews .ctrl{position:absolute;right:20px;top:22px;display:flex;gap:8px}
.reviews p{font-size:13px;line-height:1.6;margin-top:24px}
.reviews .who{color:var(--yellow);font-weight:700;margin-top:14px;font-size:13px}

/* services */
.services{position:absolute;top:888px;left:0;width:1200px;height:464px;background:linear-gradient(90deg,#cfd3d2 0%,#eef0ef 30%,#e9eae6 70%,#c5cbc6 100%)}
.services-panel{position:absolute;left:304px;top:72px;width:616px;height:320px;background:rgba(255,255,255,.78);padding:26px 40px}
.services h2{text-align:center;font-size:22px;font-weight:700;color:var(--ink)}
.service-list{display:flex;gap:40px;margin-top:26px}
.service-list ul{list-style:none;flex:1}
.service-list li{font-size:12px;color:#444;line-height:1.4;padding:6px 0 6px 20px;position:relative}
.service-list li:before{content:"";position:absolute;left:0;top:9px;width:10px;height:10px;border-radius:50%;background:var(--green)}
.services .btn{position:absolute;left:268px;top:248px}

/* gallery */
.gallery{top:1392px;height:280px}
.section-title{text-align:center;font-size:20px;font-weight:700;color:var(--ink)}
.gallery-row{display:flex;gap:24px;margin-top:30px;padding:0 14px}
.gallery-item{flex:1}
.gallery-img{height:164px;border:4px solid #fff;box-shadow:0 1px 4px rgba(0,0,0,.3)}
.gallery-item h4{color:var(--green);font-size:15px;font-weight:700;margin-top:20px;text-align:center}

/* why */
.why{position:absolute;top:1700px;left:0;width:1200px;height:452px;background:var(--grey-bg)}
.why .section-title{margin-top:40px}
.why-grid{position:absolute;left:64px;width:1072px;top:100px;display:grid;grid-template-columns:repeat(3,1fr);row-gap:40px}
.why-item{text-align:center}
.why-item svg{display:block;margin:0 auto}
.why-item p{font-size:14px;color:var(--ink);margin-top:14px}

/* footer */
.site-footer{position:absolute;top:2152px;left:0;width:1200px;height:160px;background:var(--green)}
.foot-nav{position:absolute;left:64px;top:34px;display:flex;gap:26px}
.foot-nav a{color:#fff;font-size:11px;font-weight:700;text-decoration:none}
.copy{position:absolute;left:64px;top:84px;color:#fff;font-size:11px;line-height:1.7}
.follow{position:absolute;right:64px;top:28px;color:#fff;font-size:12px;font-weight:700}
.social{display:flex;gap:6px;margin-top:10px}
.social span{width:22px;height:22px;border-radius:50%;background:var(--red)}
</style>
</head>
<body>

<header class="site-header">
  <div class="brand">
    <span class="brand-mark"></span>
    <div>
      <div class="brand-name">BRENWO TILING SOLUTIONS PTY LTD</div>
      <div class="brand-tag">WALL AND FLOOR TILING SPECIALIST</div>
    </div>
  </div>
  <div class="call">
    <svg width="20" height="20" viewBox="0 0 24 24"><path fill="#e8262b" d="M6.6 10.8a15.1 15.1 0 0 0 6.6 6.6l2.2-2.2a1 1 0 0 1 1-.25 11.4 11.4 0 0 0 3.6.57 1 1 0 0 1 1 1V20a1 1 0 0 1-1 1A17 17 0 0 1 3 4a1 1 0 0 1 1-1h3.5a1 1 0 0 1 1 1c0 1.25.2 2.45.57 3.57a1 1 0 0 1-.25 1z"/></svg>
    CALL DALTON KRUSEY ON 0400 555 218
  </div>
</header>

<nav class="container main-nav">
  <a class="active">HOME</a><a>ABOUT US</a><a>OUR SERVICES</a><a>WHY CHOOSE US</a><a>PHOTO GALLERY</a><a>REVIEWS</a><a>CONTACT US</a>
</nav>

<section class="container hero" role="img" aria-label="Photo of a tiled outdoor terrace beside a pool at dusk">
  <span class="hero-arrow" style="left:0"></span>
  <span class="hero-arrow" style="right:0"></span>
  <div class="hero-copy">
    <h1>WALL AND FLOOR TILING SPECIALIST</h1>
    <p>A Gold Coast family owned business, with over 20 years of experience</p>
  </div>
  <div class="hero-dots"><span class="on"></span><span></span><span></span><span></span></div>
</section>

<section class="container welcome">
  <div class="welcome-text">
    <h2>WELCOME TO BRENWO TILING SOLUTIONS</h2>
    <p>A Gold Coast family owned business, with over 20 years of experience, Dalton Krusey is proud to be a trusted name for all aspects of Wall and Floor Tiling Services servicing the Gold Coast to Brisbane, Tweed Heads to Mt Tamborine.</p>
    <p>With an eye for detail we strive for perfection with the resources to work closely with designers, architects, contractors, and home owners, delivering the best possible service in wall and floor tiling.</p>
  </div>
  <a class="btn">READ MORE</a>
  <aside class="reviews">
    <h3>REVIEWS</h3>
    <div class="ctrl">
      <svg width="12" height="14" viewBox="0 0 12 14"><path d="M10 1 2 7l8 6z" fill="#e8262b"/></svg>
      <svg width="12" height="14" viewBox="0 0 12 14"><path d="M2 1l8 6-8 6z" fill="#e8262b"/></svg>
    </div>
    <p>We are thrilled with our new bathroom and pool surround. Dalton was tidy, punctual and the finish is flawless. Every line is straight and every grout joint is perfect. Highly recommended to anyone renovating.</p>
    <div class="who">Tara &amp; Scott</div>
  </aside>
</section>

<section class="services" role="img" aria-label="Photo of a bright modern tiled bathroom with a freestanding bath">
  <div class="services-panel">
    <h2>OUR SERVICES</h2>
    <div class="service-list">
      <ul>
        <li>Wall and Floor Tiling – New &amp; Renovation</li>
        <li>Driveways</li>
        <li>Swimming Pools, Coping &amp; Pool Surrounds</li>
        <li>Alfresco</li>
      </ul>
      <ul>
        <li>Stone – Granite, Marble, Sandstone etc</li>
        <li>Glass Mosaics</li>
        <li>Commercial and Residential Tiling</li>
        <li>Waterproofing</li>
      </ul>
    </div>
    <a class="btn">READ MORE</a>
  </div>
</section>

<section class="container gallery">
  <h2 class="section-title">PROJECT GALLERY</h2>
  <div class="gallery-row">
    <div class="gallery-item">
      <div class="gallery-img" role="img" aria-label="Photo of a tiled bathroom floor and wall" style="background:linear-gradient(135deg,#d9d6cf,#8d8a84)"></div>
      <h4>WALL AND FLOOR TILING</h4>
    </div>
    <div class="gallery-item">
      <div class="gallery-img" role="img" aria-label="Photo of a blue tiled swimming pool with coping" style="background:linear-gradient(180deg,#7fc6e8,#1f7fc0)"></div>
      <h4>SWIMMING POOLS, COPING &amp; POOL</h4>
    </div>
    <div class="gallery-item">
      <div class="gallery-img" role="img" aria-label="Photo of a large tiled commercial floor" style="background:linear-gradient(160deg,#2b2b2b,#9a9a9a)"></div>
      <h4>COMMERCIAL AND RESIDENTIAL TILING</h4>
    </div>
  </div>
</section>

<section class="why">
  <h2 class="section-title">WHY CHOOSE US ?</h2>
  <div class="why-grid">
    <div class="why-item">
      <svg width="56" height="56" viewBox="0 0 56 56"><circle cx="28" cy="28" r="26" fill="none" stroke="#e8262b" stroke-width="2.5"/><path d="M17 29l7 7 15-16" fill="none" stroke="#e8262b" stroke-width="3.5"/></svg>
      <p>Satisfaction Guaranteed</p>
    </div>
    <div class="why-item">
      <svg width="56" height="56" viewBox="0 0 56 56"><circle cx="28" cy="28" r="26" fill="none" stroke="#e8262b" stroke-width="2.5"/><circle cx="28" cy="24" r="9" fill="none" stroke="#e8262b" stroke-width="3"/><path d="M22 32l-3 11 9-4 9 4-3-11" fill="none" stroke="#e8262b" stroke-width="3"/></svg>
      <p>Qualified Workmanship</p>
    </div>
    <div class="why-item">
      <svg width="56" height="56" viewBox="0 0 56 56"><circle cx="28" cy="28" r="26" fill="none" stroke="#e8262b" stroke-width="2.5"/><rect x="14" y="24" width="28" height="9" fill="none" stroke="#e8262b" stroke-width="3"/><path d="M20 24v4M26 24v4M32 24v4M38 24v4" stroke="#e8262b" stroke-width="2"/></svg>
      <p>Free Measure and Quote</p>
    </div>
    <div class="why-item">
      <svg width="56" height="56" viewBox="0 0 56 56"><circle cx="28" cy="28" r="26" fill="none" stroke="#e8262b" stroke-width="2.5"/><path d="M15 29l13-11 13 11M19 27v13h18V27" fill="none" stroke="#e8262b" stroke-width="3"/></svg>
      <p>Residential and Commercial Services</p>
    </div>
    <div class="why-item">
      <svg width="56" height="56" viewBox="0 0 56 56"><circle cx="28" cy="28" r="26" fill="none" stroke="#e8262b" stroke-width="2.5"/><rect x="17" y="14" width="22" height="28" fill="none" stroke="#e8262b" stroke-width="3"/><path d="M22 28l4 4 8-8" fill="none" stroke="#e8262b" stroke-width="3"/></svg>
      <p>QTRB Licenced for Wall and Floor Tiling</p>
    </div>
    <div class="why-item">
      <svg width="56" height="56" viewBox="0 0 56 56"><circle cx="28" cy="28" r="26" fill="none" stroke="#e8262b" stroke-width="2.5"/><path d="M28 13c6 9 10 14 10 20a10 10 0 0 1-20 0c0-6 4-11 10-20z" fill="none" stroke="#e8262b" stroke-width="3"/></svg>
      <p>QTRB Licenced for Waterproofing</p>
    </div>
  </div>
</section>

<footer class="site-footer">
  <nav class="foot-nav">
    <a>HOME</a><a>ABOUT US</a><a>OUR SERVICES</a><a>WHY CHOOSE US</a><a>PHOTO GALLERY</a><a>REVIEWS</a><a>CONTACT US</a>
  </nav>
  <div class="copy">Copyright © 2024 Brenwo Tiling Solutions. All Rights Reserved.<br>ABN 00 000 000 000 · QTRB Licence 000000</div>
  <div class="follow">FOLLOW US
    <div class="social"><span></span><span></span><span></span><span></span><span></span><span></span></div>
  </div>
</footer>

</body>
</html>
```